Chateau de Verbouclin multiple flyers

PRICE OFFERED IS PER FLYER IE: €139 PER FLYER OR €695 TOTAL WITH OTHERS TO FOLLOW

I want to creat a common design across a range of flyers that I will be handing out to visitors to our Christmas market, but will also be used throughout the year and years to come. The final design will need to be adapted so the copy can be translated into french as well as English. So I would need an ai or paint version as well as pdf's etc.

There are 5 flyers to be designed at this stage the PRICE OFFERED IS PER FLYER IE: €139 PER FLYER OR €695 TOTAL WITH OTHERS TO FOLLOW

1. Seminars at the chateau - 4 page 1/3 A4 double sided (No longer referring to full chateau rental)
2. Accomodation at the chateau 2 page 1/3 A4 double sided (Seasons simplified now: Peak = July & August and Christmas week; High, June and September. Low: Rest of year.)
3. VQEB 2 Diploma in Cellar Studies 4 page 1/3 A4 double sided
See current offering at
http://www.vinharbour-example.com/experiences-and-tours/wine-tours/vqeb-level-2-loire-valley-peter-anwick/#1467282665644-f1124b7e-5513

With photos here:
https://www.filecrate-example.com/sh/qpz481bnrtkaye/BBBQ9nyJRLfuF-Bdfy6thwwjb?dl=0

4. Valentine's/Romantic package 2 page 1/3 A4 double sided
5. Mothers Day package 2 page 1/3 A4 double sided.

The first two are very urgent as need to be available by Wednesday 7th December to go to print.

In the future we will be looking to add to the range with:

6. Wedding Brochure - 6 page 1/3 A4 double sided
7. Group celebrations - 6 page 1/3 A4 double sided
8. Pamper/Wellness package - 2 page 1/3 A4 double sided
9. Activity Break - 2 page 1/3 A4 double sided.

I have attached some examples of what we have to date, which are not consistent. As well as some excel spreadhseets which explain the packages. Along with an architects plan of the ground floor (may help with the seminar brochure.)

I have also provided a link to our gallery of photos that can be used and a couple of videos to give you a feel for the place.

https://www.filecrate-example.com/sh/k7rbtwqogrdhz/BBDGNXBuSplm7BHRdgbUyKb?dl=0

Target Market(s)

Adults aged 34 plus.
Seminars = Local businesses
Accommodation = 34 plus high income
Wedding = Females 28 plus high income

Requirements
Must have
• Demonstrates 5 star luxury and quality.

```html
<!DOCTYPE html>
<html lang="en">
<head>
<meta charset="utf-8">
<title>Seminars at the Chateau – Chateau de Verbouclin</title>
<link rel="stylesheet" href="https://fonts.googleapis.com/css2?family=Kaushan+Script&family=EB+Garamond:ital,wght@0,400;1,400&display=swap">
<style>
  :root {
    --backdrop: #d7e2b0;
    --paper: #fbfbfa;
    --ink: #2a2a2a;
    --ink-soft: #555555;
    --sky: #8fb8e4;
    --stone: #c9c2b3;
    --lawn: #8f8a4e;
    --vine-dark: #2f4a1f;
    --vine-mid: #5c7a2e;
    --label-bg: rgba(255, 255, 255, 0.9);
  }
  * { box-sizing: border-box; margin: 0; padding: 0; }
  html, body {
    width: 1200px;
    height: 701px;
    overflow: hidden;
    background: var(--backdrop);
  }
  .canvas {
    position: relative;
    width: 1200px;
    height: 701px;
  }
  .page {
    position: absolute;
    left: 365px;
    top: 30px;
    width: 470px;
    height: 641px;
    background: var(--paper);
    box-shadow: 0 6px 18px rgba(60, 70, 30, 0.18);
    padding: 30px 30px 0 30px;
    font-family: "EB Garamond", Georgia, serif;
    color: var(--ink);
  }
  .hero {
    position: relative;
    height: 250px;
    background:
      linear-gradient(180deg, var(--sky) 0%, #b8d0ea 38%, transparent 55%),
      linear-gradient(90deg, var(--stone) 0%, #a7a08f 30%, var(--lawn) 48%, var(--vine-mid) 55%, var(--vine-dark) 78%, #3d5a22 100%);
  }
  .hero-label {
    position: absolute;
    right: 18px;
    bottom: -14px;
    width: 190px;
    height: 60px;
    background: var(--label-bg);
    display: flex;
    align-items: center;
    justify-content: center;
    gap: 8px;
  }
  .hero-label .mark {
    width: 12px;
    height: 12px;
    background: var(--ink);
  }
  .hero-label .name {
    font-size: 11.5px;
    letter-spacing: 2.2px;
    text-transform: uppercase;
    color: var(--ink);
  }
  .intro {
    display: flex;
    gap: 22px;
    margin-top: 26px;
  }
  .title {
    flex: 0 0 160px;
    font-family: "Kaushan Script", cursive;
    font-weight: 400;
    font-size: 38px;
    line-height: 0.95;
    color: #1c1c1c;
    padding-left: 6px;
  }
  .title span { display: block; }
  .title .indent-1 { padding-left: 14px; }
  .title .indent-2 { padding-left: 26px; }
  .intro-copy {
    flex: 1;
    font-style: italic;
    font-size: 8.4px;
    line-height: 1.45;
    color: var(--ink-soft);
    padding-top: 8px;
  }
  .intro-copy p + p { margin-top: 7px; }
  .body-copy {
    margin-top: 18px;
    font-style: italic;
    font-size: 8.4px;
    line-height: 1.45;
    color: var(--ink-soft);
  }
  .body-copy p + p { margin-top: 7px; }
  .folio {
    position: absolute;
    right: 40px;
    bottom: 22px;
    font-size: 7.5px;
    color: var(--ink-soft);
    display: flex;
    gap: 14px;
  }
</style>
</head>
<body>
<main class="canvas">
  <article class="page">
    <div class="hero" role="img" aria-label="Photograph of the chateau with slate-roofed towers on the left and grape-laden vines on the right">
      <div class="hero-label">
        <span class="mark"></span>
        <span class="name">Chateau de Verbouclin</span>
      </div>
    </div>

    <section class="intro">
      <h1 class="title">
        <span>Seminars</span>
        <span class="indent-1">at the</span>
        <span class="indent-2">Chateau</span>
      </h1>
      <div class="intro-copy">
        <p>Our historic rooms offer calm, light and space for focused business meetings.</p>
        <p>Each day is shaped around your team with care.</p>
        <p>Catering, coffee breaks and evening dinners are prepared by our chef using local produce, served in the grand hall or on the terrace overlooking the vines.</p>
      </div>
    </section>

    <section class="body-copy">
      <p>Set among vineyards in the heart of the valley, the chateau welcomes groups of up to forty guests for seminars, workshops and training days. Meeting rooms come equipped with screens, high speed internet and flexible seating, while quiet lounges give space for smaller sessions.</p>
      <p>Guests can stay overnight in our elegant bedrooms, enjoy a guided tasting in the cellars and unwind with a walk through the gardens before the next day begins. Ask us for a tailored programme.</p>
    </section>

    <footer class="folio">
      <span>Seminars</span>
      <span>01</span>
    </footer>
  </article>
</main>
</body>
</html>
```